Mine Engineering Consultancy specializing in
* Pit optimization
* Mine Design
* Scheduling
* Mine Rehabilitation

Industry/Entity Type

Mining

Contact Information for Business Card

RVT Mining Pty Ltd
Derek Holloway
Director/Principle Mining Engineer
Mobile 0413582961
Email derek.holloway@rvtmining-example.com

```html
<!DOCTYPE html>
<html lang="en">
<head>
<meta charset="utf-8">
<title>RVT Mining Pty Ltd – Business Cards</title>
<link href="https://fonts.googleapis.com/css2?family=Tinos:wght@400;700&family=Open+Sans:wght@400&display=swap" rel="stylesheet">
<style>
  :root {
    --page: #e8e4de;
    --card-light: #f3f2ee;
    --pattern-tone: #e2e1dc;
    --band-dark: #272727;
    --panel-dark: #2b2b2c;
    --band-grey: #d3d3d3;
    --brand-blue: #2f6fbf;
    --ink: #1e1e1e;
    --white: #ffffff;
  }
  * { box-sizing: border-box; margin: 0; padding: 0; }
  html, body { width: 1200px; height: 900px; overflow: hidden; }
  body { background: var(--page); position: relative; font-family: "Tinos", serif; }

  .card {
    position: absolute;
    width: 640px; height: 366px;
    background: var(--card-light);
    box-shadow: 0 8px 24px rgba(0,0,0,0.18);
    overflow: hidden;
  }
  .pattern-area {
    position: absolute;
    background: linear-gradient(135deg, var(--card-light), var(--pattern-tone));
  }

  /* Name side */
  .card--name { left: 80px; top: 60px; }
  .card--name .pattern-top { left: 0; top: 0; width: 100%; height: 128px; }
  .card--name .pattern-bottom { left: 0; top: 248px; width: 100%; height: 118px; }
  .name-band {
    position: absolute; left: 0; top: 128px; width: 100%; height: 120px;
    background: var(--band-dark);
    display: flex; align-items: center; gap: 26px;
    padding-left: 96px;
  }
  .name-band .company {
    color: var(--brand-blue); font-size: 34px; font-weight: 400;
  }
  .name-band .person {
    color: var(--white); font-size: 22px;
  }

  /* Details side */
  .card--details { left: 480px; top: 474px; }
  .details-left { position: absolute; left: 0; top: 0; width: 372px; height: 100%; }
  .details-left .pattern-area { left: 0; top: 0; width: 100%; height: 100%; }
  .job-title {
    position: absolute; left: 24px; top: 30px;
    font-size: 19px; color: var(--ink);
  }
  .identity-band {
    position: absolute; left: 0; top: 80px; width: 100%; height: 150px;
    background: var(--band-grey);
    padding: 34px 0 0 28px;
  }
  .identity-band .company { color: var(--brand-blue); font-size: 28px; }
  .identity-band .person { color: var(--ink); font-size: 26px; margin-top: 8px; }

  .details-right {
    position: absolute; left: 372px; top: 0; width: 268px; height: 100%;
    background: var(--panel-dark);
    padding: 22px 14px 0 22px;
  }
  .services-heading {
    color: var(--brand-blue); font-weight: 700; font-size: 20px; line-height: 1.25;
  }
  .services {
    list-style: none; margin: 12px 0 0 20px;
    color: var(--white); font-size: 19px; line-height: 1.45;
  }
  .services li::before { content: "* "; }
  .contact {
    list-style: none; margin-top: 20px;
    font-family: "Open Sans", sans-serif; color: var(--white); font-size: 11.5px;
  }
  .contact li { display: flex; align-items: center; gap: 10px; margin-bottom: 12px; }
  .contact svg { flex: none; }
</style>
</head>
<body>

  <section class="card card--name">
    <div class="pattern-area pattern-top" role="img" aria-label="Light grey interlocking key pattern"></div>
    <div class="name-band">
      <span class="company">RVT Mining Pty Ltd</span>
      <span class="person">Derek Holloway</span>
    </div>
    <div class="pattern-area pattern-bottom" role="img" aria-label="Light grey interlocking key pattern"></div>
  </section>

  <section class="card card--details">
    <div class="details-left">
      <div class="pattern-area" role="img" aria-label="Light grey interlocking key pattern"></div>
      <p class="job-title">Director/Principle Mining Engineer</p>
      <div class="identity-band">
        <p class="company">RVT Mining Pty Ltd</p>
        <p class="person">Derek Holloway</p>
      </div>
    </div>
    <div class="details-right">
      <h2 class="services-heading">Mine Engineering Consultancy specializing:-</h2>
      <ul class="services">
        <li>Pit optimization</li>
        <li>Mine Design</li>
        <li>Scheduling</li>
        <li>Mine Rehabilitation</li>
      </ul>
      <ul class="contact">
        <li>
          <svg width="24" height="16" viewBox="0 0 24 16" aria-hidden="true">
            <rect x="0" y="0" width="24" height="16" rx="1" fill="var(--brand-blue)"/>
            <path d="M1 1 L12 9 L23 1" fill="none" stroke="var(--panel-dark)" stroke-width="1.6"/>
          </svg>
          <span>derek.holloway@rvtmining-example.com</span>
        </li>
        <li>
          <svg width="20" height="20" viewBox="0 0 24 24" aria-hidden="true">
            <path fill="var(--brand-blue)" d="M6.6 10.8a15.1 15.1 0 0 0 6.6 6.6l2.2-2.2a1 1 0 0 1 1-.25 11.4 11.4 0 0 0 3.6.57 1 1 0 0 1 1 1V20a1 1 0 0 1-1 1A17 17 0 0 1 3 4a1 1 0 0 1 1-1h3.5a1 1 0 0 1 1 1c0 1.25.2 2.45.57 3.57a1 1 0 0 1-.25 1z"/>
          </svg>
          <span>0413582961</span>
        </li>
      </ul>
    </div>
  </section>

</body>
</html>
```